International Property Consultancy

Brief Overview:

I need a dynamic and well designed website that is easy to use and understand. It has to be unique and different to generic templates that most websites seem to be these days. PLEASE NO GENERIC TEMPLATES FROM THE INTERNET.

Our business has 10 years experience working on struggling international developments that we then work in-house for to turn around and brings bout success. We stay within a project often for long periods of time until success is achieved. We are unique in our approach and completely different to the standard routes to market for many developments. The site is for developers to see what we have done in regards to previous projects, as such we want to incorporate video into this site with a strong design aesthetic. There will be videos of the past projects we have worked on, which will act as case studies.

I like very simple but punchy websites, that people can navigate and understand very easily. Also a big fan of unique and well thought out design aesthetic.

Initial Site layout thoughts:

1) Homepage:
2) About Us
3) What we've done / Work
This part has the projects we have worked on (France, Portugal, London, Morocco). Each one will have some video content and photo images, but also would be good to have a succinct way to mention what we did and the successes in a clever and punchy way.

4) Contact Us

* This is just a guideline. Would be open to input and creative direction on your own part.

*More details and websites we like can be seen in the brief doc attached.

PLEASE VIEW THE WIREFRAME WORD DOC ATTACHED.

Here there are also some more examples to help:

Here are just a few examples of websites and what I like about them:

- www.velmoro.com (clean, nice geometric design aesthetic, good animation when loading and changing pages well thought out all though also coulee be considered a bit dull and basic after the initial homepage slide)
- https://www.farbridgehub.net (Clean site, quite clinical, lacks video content and doesn't engage greatly).
- https://ruskotile.com (minimal, and like how it mixes the design aesthetic more with video and photo content)

- https://www.amberquillworks.com (like the layout of this and how it displays the projects and work section)

- https://brisk.com (Good use of video content)

- https://loomfield.studio (minimal to the point and mixes design with video and animation etc...)

Here is another couple of cool websites that may help give you some direction: https://halvenquay.com www.brisk.com

Hi there, One of the things I thought would be good on the homepage is to add the logo with a 'digital landscape' before flicking down into a slide with video content of the projects... Just an idea but have posted some pics in the brief. We would get this animated for the site. But if you have better ideas, please do run with them. Thanks,

Target Market(s)

Property developers

Number of Pages Required

4 page

Font styles to use
Other font styles liked:
• Read brief

Requirements
Must have
• Needs to be clean, dynamic and easy to follow on desktop and mobile. We will use it as a kind of portfolio website so will need to embed video of past projects we have worked on.

Read brief in docs.
Nice to have
• Clean
Should not have
• Not be another generic template website.
Not have random property stock photos. (We are not a property agency).

```html
<!DOCTYPE html>
<html lang="en">
<head>
<meta charset="utf-8">
<title>Calvorin — International Property Consultancy</title>
<link href="https://fonts.googleapis.com/css2?family=Montserrat:wght@400;500;600;700;800&display=swap" rel="stylesheet">
<style>
:root{
  --teal:#1e7390;
  --button:#2490b5;
  --ink:#2b2b2b;
  --muted:#a7a7a7;
  --field:#e6e6e6;
  --footer:#f8e1da;
  --white:#ffffff;
}
*{box-sizing:border-box;margin:0;padding:0}
html,body{width:1200px;height:2250px;overflow:hidden}
body{position:relative;font-family:'Montserrat',sans-serif;color:var(--ink);background:var(--white)}
.abs{position:absolute}

/* hero */
.hero{left:0;top:0;width:1200px;height:584px;
  background:radial-gradient(ellipse at 50% 45%,#4a5a66 0%,#2e3a44 40%,#151a1f 80%);}
.brand{left:148px;top:4px;font-size:36px;font-weight:500;color:var(--white);letter-spacing:0.5px}
.search{left:1033px;top:22px}
.hero-title{left:200px;top:174px;width:800px;text-align:center;color:var(--white);
  font-size:24px;font-weight:800;line-height:36px}
.play{left:600px;top:319px;text-align:center;color:var(--white);font-size:12px;font-weight:600}
.play svg{display:block;margin:0 auto 5px}

/* side navigation */
.side-nav{left:148px;width:120px}
.side-nav .rail{position:absolute;left:2px;top:8px;width:1px;background:var(--muted)}
.side-nav .item{position:absolute;left:0;font-size:14px;color:var(--muted);padding-left:12px;white-space:nowrap}
.side-nav .item::before{content:"";position:absolute;left:0;top:7px;width:5px;height:5px;border-radius:50%;background:var(--muted)}
.side-nav .item.active{color:var(--teal);font-weight:600}
.side-nav .item.active::before{background:var(--teal)}
.side-nav.light .rail{background:#cfd3d6}
.side-nav.light .item{color:#e8e8e8;font-weight:500}
.side-nav.light .item::before{background:#e8e8e8}
.side-nav.light .item.active{color:#2b98bd}
.side-nav.light .item.active::before{background:#2b98bd}

/* about */
.about-title{left:286px;top:829px;width:600px;font-size:19px;font-weight:700;color:var(--teal);line-height:22px}
.about-text{left:286px;top:897px;width:650px;font-size:14px;line-height:22.5px;color:var(--ink)}

/* headings with underline */
.section-title{font-size:19px;font-weight:700;color:var(--teal);padding-bottom:3px;border-bottom:3px solid var(--teal)}

/* project */
.project-text{left:286px;top:1370px;width:390px;font-size:14px;line-height:27px}
.pager{top:1586px;font-size:12.5px;color:var(--teal);font-weight:500}
.pager-count{left:470px;top:1589px;font-size:11px;color:var(--ink)}
.project-media{left:684px;top:1235px;width:366px;height:367px;
  background:linear-gradient(180deg,#18283a 0%,#1f3346 45%,#2a2f38 75%,#11161c 100%)}
.project-media .icon{position:absolute;left:171px;top:170px}

/* contact */
.field{background:var(--field);font-size:10px;color:#6f6f6f;padding:12px 8px 0}
.send{left:287px;top:2075px;width:130px;height:30px;background:var(--button);color:var(--white);
  font-size:14px;font-weight:700;text-align:center;line-height:30px}
.social{left:836px;font-size:13px;color:var(--ink);display:flex;align-items:center;gap:12px}
.social .dot{width:18px;height:18px;border-radius:50%;background:var(--ink)}

.footer{left:0;top:2207px;width:1200px;height:43px;background:var(--footer);
  text-align:center;line-height:43px;font-size:11px;color:#555}
</style>
</head>
<body>

<section class="abs hero" role="img" aria-label="Upward view of glass skyscrapers against a dusky sky"></section>
<div class="abs brand">calvorin.</div>
<svg class="abs search" width="18" height="18" viewBox="0 0 18 18" fill="none" stroke="#fff" stroke-width="1.5">
  <circle cx="7.5" cy="7.5" r="5.5"/><line x1="11.5" y1="11.5" x2="16" y2="16"/>
</svg>
<h1 class="abs hero-title">Consultancy Company That Helps International Property Developments Fulfil Their Potential.</h1>
<div class="abs play" style="transform:translateX(-50%)">
  <svg width="26" height="26" viewBox="0 0 26 26" fill="none" stroke="#fff" stroke-width="1.4">
    <circle cx="13" cy="13" r="12"/><path d="M10.5 8.5 L17 13 L10.5 17.5 Z"/>
  </svg>
  Play Vedio
</div>

<nav class="abs side-nav light" style="top:186px;height:220px">
  <span class="rail" style="height:202px"></span>
  <span class="item active" style="top:0">Home</span>
  <span class="item" style="top:67px">About Us</span>
  <span class="item" style="top:134px">Projects</span>
  <span class="item" style="top:202px">Contact Us</span>
</nav>

<!-- about -->
<nav class="abs side-nav" style="top:765px;height:220px">
  <span class="rail" style="height:202px"></span>
  <span class="item" style="top:0">Home</span>
  <span class="item active" style="top:67px">About Us</span>
  <span class="item" style="top:134px">Projects</span>
  <span class="item" style="top:202px">Contact Us</span>
</nav>
<h2 class="abs about-title">We specialise in the fulfilment of international property developments.</h2>
<p class="abs about-text">Calvorin is a consultancy company that helps international property developments fulfil their potential. The company has had great success over the last 10 years of turning around struggling property developments (often resort and investment) and making them reach their maximum potential.<br>We have completed projects in Portugal, London, France, Morocco, Brazil...</p>

<!-- projects -->
<h2 class="abs section-title" style="left:286px;top:1261px">France</h2>
<nav class="abs side-nav" style="top:1322px;height:220px">
  <span class="rail" style="height:203px"></span>
  <span class="item" style="top:0">Home</span>
  <span class="item" style="top:67px">About Us</span>
  <span class="item active" style="top:135px">Projects</span>
  <span class="item" style="top:203px">Contact Us</span>
</nav>
<p class="abs project-text">Lorem ipsum dolor sit amet, consectetur adipiscing elit, sed do eiusmod tempor incididunt ut labore et dolore magna aliqua. Quis ipsum suspendisse ultrices gravida. Risus commodo viverra maecenas accumsan lacus vel facilisis.</p>
<div class="abs pager" style="left:286px">&lsaquo;&nbsp; Prev Project</div>
<div class="abs pager-count">1/4</div>
<div class="abs pager" style="left:583px">Next Project &nbsp;&rsaquo;</div>
<div class="abs project-media" role="img" aria-label="City skyline at night across the water">
  <svg class="icon" width="26" height="26" viewBox="0 0 26 26" fill="none" stroke="#fff" stroke-width="1.4">
    <circle cx="13" cy="13" r="12"/><path d="M10.5 8.5 L17 13 L10.5 17.5 Z"/>
  </svg>
</div>

<!-- contact -->
<h2 class="abs section-title" style="left:287px;top:1819px">Contacts</h2>
<h2 class="abs section-title" style="left:834px;top:1819px">Fallow Us</h2>
<nav class="abs side-nav" style="top:1888px;height:220px">
  <span class="rail" style="height:203px"></span>
  <span class="item" style="top:0">Home</span>
  <span class="item" style="top:67px">About Us</span>
  <span class="item" style="top:135px">Projects</span>
  <span class="item active" style="top:203px">Contact Us</span>
</nav>
<div class="abs field" style="left:287px;top:1895px;width:260px;height:30px">Your Name*</div>
<div class="abs field" style="left:562px;top:1895px;width:259px;height:30px">Last Name*</div>
<div class="abs field" style="left:287px;top:1940px;width:260px;height:30px">Company Name*</div>
<div class="abs field" style="left:562px;top:1940px;width:259px;height:30px">E-mail*</div>
<div class="abs field" style="left:287px;top:1985px;width:534px;height:75px;padding-top:8px">Message</div>
<div class="abs send">Send</div>

<div class="abs social" style="top:1903px"><span class="dot"></span>www.friendwall.com/Calvorin</div>
<div class="abs social" style="top:1942px"><span class="dot"></span>www.chirpline.com/Calvorin</div>
<div class="abs social" style="top:1981px"><span class="dot"></span>www.worklinkr.com/Calvorin</div>
<div class="abs social" style="top:2021px"><span class="dot"></span>www.pinboardly.com/Calvorin</div>

<footer class="abs footer">Copyright © 2020 Calvorin</footer>

</body>
</html>
```